Kestrel Gardenworks Business Card

An eye catching, yet simple business card that includes;

1. our logo
2. office phone - 5083172946
3. email - kestrelgardenworks@mailbrook.com
4. website - www.kestrelgardenworks.com
5. instagram - @kestrelgardenworksnv

```html
<!DOCTYPE html>
<html lang="en">
<head>
<meta charset="utf-8">
<title>Kestrel Gardenworks Business Card</title>
<link href="https://fonts.googleapis.com/css2?family=Lato:wght@400;700;900&display=swap" rel="stylesheet">
<style>
  :root {
    --page: #e9e6e4;
    --card-light: #e4e0df;
    --card-mid: #cfc9c8;
    --sheen: #f7f5f4;
    --ink: #1c1a1a;
    --brand-brown: #7a3b1c;
    --band-light: #a88266;
    --band-dark: #6c3317;
    --band-end: #7b4429;
    --band-text: #f3e9e2;
  }
  * { margin: 0; padding: 0; box-sizing: border-box; }
  html, body {
    width: 1200px;
    height: 734px;
    overflow: hidden;
    background: var(--page);
    font-family: "Lato", sans-serif;
  }
  .card {
    position: absolute;
    left: 40px;
    top: 46px;
    width: 1120px;
    height: 643px;
    border-radius: 6px 26px 26px 6px;
    overflow: hidden;
    background:
      radial-gradient(ellipse 260px 320px at 150px 120px, var(--sheen), transparent 70%),
      linear-gradient(180deg, var(--card-light), var(--card-mid));
    box-shadow: 0 0 0 1.5px rgba(255,255,255,0.8), 0 10px 30px rgba(0,0,0,0.12);
  }
  .hero-art {
    position: absolute;
    left: 0;
    top: 36px;
    width: 686px;
    height: 527px;
    border-radius: 0 120px 40px 0;
    background:
      radial-gradient(ellipse 360px 240px at 440px 230px, rgba(20,18,18,0.85), rgba(20,18,18,0.35) 60%, transparent 80%),
      linear-gradient(90deg, rgba(60,58,58,0.25), rgba(30,28,28,0.45));
  }
  .brand {
    position: absolute;
    left: 640px;
    top: 178px;
    width: 420px;
    display: flex;
    align-items: center;
    gap: 16px;
  }
  .brand-dot {
    width: 34px;
    height: 34px;
    border-radius: 50%;
    background: var(--brand-brown);
    flex: none;
  }
  .brand-name {
    font-weight: 900;
    font-size: 50px;
    line-height: 1.02;
    color: var(--brand-brown);
  }
  .contact-band {
    position: absolute;
    left: 0;
    top: 409px;
    width: 100%;
    height: 234px;
    clip-path: polygon(116px 0, 100% 0, 100% 100%, 59px 100%);
    background: linear-gradient(90deg, var(--band-light) 10%, var(--band-dark) 48%, var(--band-end) 100%);
  }
  .person {
    position: absolute;
    left: 162px;
    top: 456px;
    color: var(--band-text);
  }
  .person-name {
    font-weight: 700;
    font-size: 45px;
    letter-spacing: 0.5px;
    line-height: 1.1;
  }
  .person-role {
    font-weight: 400;
    font-size: 27px;
    line-height: 1.3;
  }
  .contact-list {
    position: absolute;
    left: 628px;
    top: 456px;
    list-style: none;
    color: var(--band-text);
    font-size: 25px;
    letter-spacing: 0.6px;
  }
  .contact-item {
    display: flex;
    align-items: center;
    height: 39.5px;
  }
  .contact-icon {
    width: 22px;
    height: 22px;
    margin-right: 18px;
    flex: none;
    fill: var(--band-text);
  }
  .social-mark {
    width: 20px;
    height: 20px;
    margin: 0 19px 0 1px;
    border-radius: 3px;
    background: var(--band-text);
    flex: none;
  }
</style>
</head>
<body>
  <main class="card">
    <div class="hero-art" role="img" aria-label="Large dark leaping kangaroo illustration"></div>

    <div class="brand">
      <span class="brand-dot"></span>
      <span class="brand-name">Kestrel<br>Gardenworks</span>
    </div>

    <div class="contact-band"></div>

    <div class="person">
      <p class="person-name">DANA HOLLIS</p>
      <p class="person-role">Creative Director</p>
    </div>

    <ul class="contact-list">
      <li class="contact-item">
        <svg class="contact-icon" viewBox="0 0 24 24" aria-hidden="true"><path d="M6.6 10.8a15.1 15.1 0 0 0 6.6 6.6l2.2-2.2a1 1 0 0 1 1-.25 11.4 11.4 0 0 0 3.6.57 1 1 0 0 1 1 1V20a1 1 0 0 1-1 1A17 17 0 0 1 3 4a1 1 0 0 1 1-1h3.5a1 1 0 0 1 1 1c0 1.25.2 2.45.57 3.57a1 1 0 0 1-.25 1z"/></svg>
        <span>5083172946</span>
      </li>
      <li class="contact-item">
        <svg class="contact-icon" viewBox="0 0 24 24" aria-hidden="true"><path d="M2 5h20v2l-10 6L2 7z M2 9l10 6 10-6v10H2z"/></svg>
        <span>kestrelgardenworks@mailbrook.com</span>
      </li>
      <li class="contact-item">
        <svg class="contact-icon" viewBox="0 0 24 24" aria-hidden="true"><path d="M12 2a10 10 0 1 0 0 20 10 10 0 0 0 0-20zm-1 17.9A8 8 0 0 1 4.2 10.2L9 15v1a2 2 0 0 0 2 2zm6.9-2.5A2 2 0 0 0 16 16h-1v-3a1 1 0 0 0-1-1H8v-2h2a1 1 0 0 0 1-1V7h2a2 2 0 0 0 2-2v-.4a8 8 0 0 1 2.9 12.8z"/></svg>
        <span>www.kestrelgardenworks.com</span>
      </li>
      <li class="contact-item">
        <span class="social-mark"></span>
        <span>@kestrelgardenworksnv</span>
      </li>
    </ul>
  </main>
</body>
</html>
```